New Letterhead Design Project

i need a logo letterhead & compliment slips for my new company the name of the company is called Harwick Civil Engineers Ltd the work we do is foundations floor slabs drainage retaining walls block paving & tarmac

Industry/Entity Type

It Company

```html
<!DOCTYPE html>
<html lang="en">
<head>
<meta charset="utf-8">
<title>Harwick Civil Engineers Ltd — Letterhead</title>
<link rel="stylesheet" href="https://fonts.googleapis.com/css2?family=Arimo:wght@400;700&display=swap">
<style>
  :root {
    --paper: #ffffff;
    --brand-red: #d71920;
    --brand-navy: #1d3f8f;
    --sky-blue: #2e8fe0;
    --pale-blue: #a9d3f5;
    --mist-blue: #d6ebfb;
    --rust: #c2584a;
    --ink: #1a1a1a;
    --mark-grey: #6d6e71;
  }
  html, body {
    margin: 0;
    padding: 0;
    overflow: hidden;
    background: var(--paper);
  }
  .letterhead {
    position: relative;
    width: 849px;
    height: 1200px;
    overflow: hidden;
    background: var(--paper);
    font-family: "Arimo", Arial, sans-serif;
  }
  .frame {
    position: absolute;
    inset: 0;
    width: 849px;
    height: 1200px;
  }
  .brand {
    position: absolute;
    left: 22px;
    top: 26px;
    display: flex;
    align-items: center;
    gap: 18px;
  }
  .brand-dot {
    width: 92px;
    height: 92px;
    border-radius: 50%;
    background: var(--mark-grey);
  }
  .brand-name {
    margin: 0;
    font-weight: 700;
    font-size: 33px;
    line-height: 1.08;
    color: var(--brand-red);
    letter-spacing: -0.3px;
  }
  .footer-name {
    position: absolute;
    left: 10px;
    top: 1168px;
    margin: 0;
    font-size: 21px;
    color: var(--ink);
  }
</style>
</head>
<body>
<main class="letterhead">
  <svg class="frame" viewBox="0 0 849 1200" xmlns="http://www.w3.org/2000/svg">
    <defs>
      <linearGradient id="skylineFade" x1="0" y1="0" x2="1" y2="0">
        <stop offset="0" stop-color="#ffffff" stop-opacity="0"/>
        <stop offset="0.45" stop-color="#bfe0f8"/>
        <stop offset="1" stop-color="#3d9be6"/>
      </linearGradient>
      <linearGradient id="bottomSkyline" x1="0" y1="0" x2="1" y2="0">
        <stop offset="0" stop-color="#e3b1a6" stop-opacity="0.4"/>
        <stop offset="1" stop-color="#c2584a"/>
      </linearGradient>
      <linearGradient id="baseSweep" x1="0" y1="0" x2="1" y2="0">
        <stop offset="0" stop-color="#1f7fd6"/>
        <stop offset="1" stop-color="#6fb8f0"/>
      </linearGradient>
    </defs>

    <!-- city skyline band, top right -->
    <rect class="skyline-top" role="img" aria-label="Pale blue city skyline silhouette"
          x="320" y="40" width="440" height="150" fill="url(#skylineFade)"/>

    <!-- right edge stripes -->
    <polygon class="stripe-pale" points="752,0 800,0 822,1060 806,1060" fill="var(--pale-blue)"/>
    <polygon class="stripe-sky" points="790,0 806,0 826,1040 818,1040" fill="var(--sky-blue)"/>
    <polygon class="stripe-red" points="818,0 838,0 849,720 849,880" fill="var(--brand-red)"/>
    <polygon class="stripe-navy" points="840,0 849,0 849,1200 846,1200" fill="var(--brand-navy)"/>

    <!-- bottom city skyline -->
    <rect class="skyline-bottom" role="img" aria-label="Terracotta city skyline silhouette"
          x="280" y="1115" width="569" height="60" fill="url(#bottomSkyline)"/>

    <!-- bottom sweep bands -->
    <polygon class="sweep-light" points="0,1130 849,1070 849,1085 0,1140" fill="var(--mist-blue)"/>
    <polygon class="sweep-main" points="0,1142 849,1086 849,1102 0,1158" fill="url(#baseSweep)"/>
  </svg>

  <header class="brand">
    <div class="brand-dot" aria-hidden="true"></div>
    <h1 class="brand-name">Harwick Civil<br>Engineers Ltd.</h1>
  </header>

  <p class="footer-name">harwick civil engineers ltd.</p>
</main>
</body>
</html>
```